Lens Harbor Teutonia Website - Photography and Films

We are looking for a design that expresses the friendly, open nature of our company Lens Harbor Teutonia, yet at the same time is professional looking and functional.

Lens Harbor Teutonia is a B2B focused operation that hires out multi-lingual camera crews (and equipment) throughout Germany and Europe. We also produce tv features and coporate films. Our unique selling point is that we are native English speakers who can communicate with our international clients (usually British or American) and organise the logistics of shooting in foreign countries.

For content inspiration, see our current website: http://www.lensharborteutonia.com - however we want to move away from the very simple structure of this site and move towards a layout that displays and allows for frequently updated content (e.g. in the form of a blog).

Here is an example of the kind of clean look we like:
http://www.qrvpixelarchive.com/archive/main/reelsqrv.do#reel=48213760

Please keep within the following specifications:
- We wish to keep our logo (grey/white, font: Glypha) and our company colour red (#C40A0A) as they are.
- Maximum Width 960px, on a large browser-window the design should be centred
- Easily readable font sizes with good contrast
- Provide your design in PSD file format
- Our logo should be graphically displayed in the top left of the header.
- The design should allow space for a video.
- The page should have a clearly recognisable end in the form of a footer.

The following menu items need to be clearly arranged so the viewer is not overwhelmed or confused:
About
Services - Crews / Corporate Shoots / Webcasts / Production Arm / Legal Videography
Recent Productions
Blog
Testimonials
Get a Quote
Contact
Film Library
Showreel
Events
Film Location Guide - Frankfurt / Cologne / Zurich / Helsinki / Amsterdam / London / Paris / Rome / Brussels / Berlin / Munich
Updates

Reason: Hi - thanks very much for your interest in our design project.  We are extending this auction because we haven't had enough time to really focus on the desigs and provide immediate feedback to designers.  We will try to provide timely feedback and are giving you more time to make any adjustments to your designs etc.
Thanks!
Marla

Target Market(s)

Our target customers are males and females between 25 and 55 years (mostly British and American). More important than their demographic though, is their occupation - they are largely communication and design savvy individuals belonging to one of the following three categories: 1)Broadcasters (usually producers for example from the QRV or Horizon Vista TV seeking trustworthy, affordable crews for their foreign shoots).

2) Video Production Companies (seeking a trustworthy, affordable partner company to provide the crews for their own corporate clients).

3) Corporate Communications Specialists (seeking professional producers and crews to facilitate production of company videos or filming of events).

Industry/Entity Type

Camera

Requirements
Must have
• A fresh clean appearance with good use of white space.
Should not have
• Avoid dark heavy colours and designs.
• Avoid designs that would be impractical and could potentially take a long time to load.

```html
<!DOCTYPE html>
<html lang="en">
<head>
<meta charset="utf-8">
<title>Lens Harbor Teutonia</title>
<link href="https://fonts.googleapis.com/css2?family=Open+Sans:wght@400;700;800&family=Questrial&family=Varela+Round&display=swap" rel="stylesheet">
<style>
:root{
  --red:#c40a0a;
  --red-dark:#9c0808;
  --red-light:#e84848;
  --white:#ffffff;
  --ink:#111111;
  --grey:#8a8a8a;
  --rule:#cfcfcf;
  --tab:#f2f2f2;
}
*{margin:0;padding:0;box-sizing:border-box}
html,body{width:1061px;height:1200px;overflow:hidden;background:var(--white)}
body{position:relative;font-family:"Open Sans",sans-serif;color:var(--ink)}
.abs{position:absolute}
.topbar{left:0;top:0;width:1061px;height:24px;background:var(--red-dark)}
.toplinks{right:100px;top:5px;font-size:9.5px;color:var(--white);letter-spacing:.2px}
.header{left:0;top:24px;width:1061px;height:86px;background:linear-gradient(#d81616,#c40a0a 60%,#b30707)}
.logo{left:70px;top:44px;font-family:"Open Sans",sans-serif;font-weight:800;font-size:28px;color:var(--white);letter-spacing:-.3px}
.nav{left:461px;top:54px;display:flex;font-family:"Questrial",sans-serif;font-size:15px;color:var(--white)}
.nav a{color:inherit;text-decoration:none;padding:5px 8px 6px;margin-right:4px}
.nav a.current{background:#a80808}
.hero{left:0;top:110px;width:1061px;height:316px;background:linear-gradient(90deg,#c40a0a 0%,#e34444 50%,#c40a0a 100%);border-bottom:2px solid #a40707}
.hero-shadow{left:130px;top:426px;width:800px;height:18px;background:radial-gradient(ellipse at top,rgba(0,0,0,.22),rgba(0,0,0,0) 70%)}
.hero-media{left:70px;top:127px;width:416px;height:276px;border:3px solid var(--white);background:linear-gradient(135deg,#3a3632,#7d7468 45%,#1e1c1a);box-shadow:0 1px 4px rgba(0,0,0,.4)}
.hero-title{left:544px;top:146px;font-family:"Varela Round",sans-serif;font-weight:700;font-size:31px;line-height:41px;color:var(--white);text-shadow:0 1px 1px rgba(0,0,0,.25)}
.hero-text{left:550px;top:280px;width:430px;font-size:12px;line-height:15.5px;color:var(--white)}
.btn{left:549px;top:345px;width:97px;height:32px;background:linear-gradient(#d81818,#b30707);border:1px solid #e45050;border-radius:3px;color:var(--white);font-size:12px;text-align:center;line-height:30px;box-shadow:0 1px 2px rgba(0,0,0,.3)}
.welcome-title{left:147px;top:465px;font-family:"Questrial",sans-serif;font-size:22px}
.welcome-text{left:147px;top:497px;width:475px;font-size:10.5px;line-height:15.1px}
.call{left:146px;top:638px;font-family:"Questrial",sans-serif;font-size:20.5px;line-height:25px}
.divider{left:147px;top:725px;width:521px;height:1px;background:var(--rule)}
.sidemenu{left:733px;top:463px;width:175px;border:1px solid #d2d2d2;border-radius:6px;overflow:hidden;background:var(--white);box-shadow:0 1px 3px rgba(0,0,0,.12)}
.sidemenu div{height:25.2px;line-height:26px;text-align:center;font-size:12.5px;background:linear-gradient(#ffffff,#e9e9e9);border-bottom:1px solid #d8d8d8}
.sidemenu div:last-child{border-bottom:0}
.testi-title{left:147px;top:736px;font-family:"Questrial",sans-serif;font-size:22px}
.card{top:771px;width:164px}
.card .photo{width:164px;height:112px;border:1px solid #cfcfcf;padding:2px;background-clip:content-box}
.card .who{margin-top:6px;font-size:10.5px;line-height:15px;font-weight:700}
.card .who span{font-weight:700}
.card p{margin-top:5px;font-size:9.2px;line-height:11.8px;letter-spacing:.15px}
.vsep{top:778px;width:1px;height:215px;background:#e4e4e4}
.footer{left:0;top:1008px;width:1061px;height:160px;background:var(--red)}
.footbar{left:0;top:1168px;width:1061px;height:32px;background:var(--red-dark);color:var(--white);font-size:11px;text-align:center;line-height:30px}
.fcol{top:1043px;color:var(--white)}
.fcol h4{font-family:"Arial",sans-serif;font-weight:400;font-size:14px;margin-bottom:9px;font-family:"Open Sans",sans-serif}
.fcol li{list-style:none;font-size:11px;height:17px;display:flex;align-items:center}
.fcol li svg{margin-right:5px}
.social{left:769px;top:1079px;display:grid;grid-template-columns:repeat(3,32px);gap:5px 8px}
.social span{width:32px;height:32px;border-radius:6px;border:2px solid #ffffff33;display:block}
</style>
</head>
<body>
<div class="abs topbar"></div>
<div class="abs toplinks">home | showreel | production arm | legal videography | contact |</div>
<div class="abs header"></div>
<div class="abs logo">Lensharborteutonia</div>
<nav class="abs nav">
  <a class="current">Home</a><a>Showreel</a><a>Production arm</a><a>Legal videography</a><a>Contact Us</a>
</nav>

<section class="abs hero"></section>
<div class="abs hero-shadow"></div>
<div class="abs hero-media" role="img" aria-label="Camera operator filming two men in a broadcast studio"></div>
<h1 class="abs hero-title">English Speaking<br>Camera Crews Throughout<br>Germany and Europe</h1>
<p class="abs hero-text">We set up Lens Harbor Teutonia to meet the demands of a growing number of TV-producers whose working language is English. This is our Passion! Why else would we keep doing it for over 30 years!</p>
<div class="abs btn">Read More</div>

<h2 class="abs welcome-title">Welcome To Our Website</h2>
<p class="abs welcome-text">As a producer, you're bound to have great ideas...but how do you make them a reality in a country where you can't speak the language? Partner with us!<br>We are native English speakers so nothing gets lost in translation. We'll catch hold of your vision, and with local know-how, we'll make it happen. No job is too big, too small too hard, too far away, or too urgent. Try us!<br>We provide camera crews and facilities throughout Germany and Europe we shoot in both PAL and NTSC We edit either in-studio or on the move and we transfer urgent footage via FTP or SNG We are on call 24/7 To make a no obligation enquiry about any of our services.</p>
<p class="abs call">Please call our Frankfurt Headquarters: +49-69-000000<br>(Toll free from the USA 1-800-555-0199)<br>or click here to get a quote.</p>
<div class="abs divider"></div>

<div class="abs sidemenu">
  <div>About Us</div><div>Our Services</div><div>Recent Productions</div><div>Our Blog</div><div>Testimonials</div><div>Get a Quote</div><div>Contact us</div><div>Film Library</div><div>Film Location Guide</div><div>Events</div>
</div>

<h2 class="abs testi-title">Testimonial</h2>

<div class="abs card" style="left:143px">
  <div class="photo" role="img" aria-label="Producer with a camera crew on location" style="background-color:#8a5a48"></div>
  <div class="who">Rhea Corwin, producer<br>Bright Field, USA</div>
  <p>I can't say enough about my crew in Europe. They were - by far - the best crew I've ever worked with! Prepared, efficient, accommodating, funny, nice, affordable.</p>
</div>
<div class="abs vsep" style="left:324px"></div>
<div class="abs card" style="left:344px">
  <div class="photo" role="img" aria-label="Two producers smiling on a street" style="background-color:#6e6a66"></div>
  <div class="who">Tess Marlow, Senior Producer<br>Northwind News</div>
  <p>Working with Lens Harbor Teutonia has been an amazing experience.Working with Lens Harbor Teutonia has been an amazing experi-ence.</p>
</div>
<div class="abs vsep" style="left:524px"></div>
<div class="abs card" style="left:543px">
  <div class="photo" role="img" aria-label="Producer standing in front of a lit display wall" style="background-color:#3d3a4a"></div>
  <div class="who">Nora Pike, producer K/LM<br>New York</div>
  <p>Its been a real pleasure working with Lens Harbor Teutonia, they are really great! They took care of all our needs, got every-thing we needed at very short notice.</p>
</div>
<div class="abs vsep" style="left:722px"></div>
<div class="abs card" style="left:738px">
  <div class="photo" role="img" aria-label="Presenter in a suit in a church interior" style="background-color:#4a4640"></div>
  <div class="who">Grant Hollis, Presenter<br>Northwind News</div>
  <p>I am Grant Hollis and this has been another great shoot with Lens Harbor Teutonia, the kind of work that we've come to ap-preciate at Fieldnotes on Northwind News Channel.</p>
</div>

<footer class="abs footer"></footer>
<div class="abs fcol" style="left:145px"><h4>Home</h4><ul>
<li><svg width="11" height="8" viewBox="0 0 11 8"><path d="M0 0l4 4-4 4M5 0l4 4-4 4" fill="none" stroke="#fff" stroke-width="2"/></svg>Link 1</li>
<li><svg width="11" height="8" viewBox="0 0 11 8"><path d="M0 0l4 4-4 4M5 0l4 4-4 4" fill="none" stroke="#fff" stroke-width="2"/></svg>Link 1</li>
<li><svg width="11" height="8" viewBox="0 0 11 8"><path d="M0 0l4 4-4 4M5 0l4 4-4 4" fill="none" stroke="#fff" stroke-width="2"/></svg>Link 1</li>
<li><svg width="11" height="8" viewBox="0 0 11 8"><path d="M0 0l4 4-4 4M5 0l4 4-4 4" fill="none" stroke="#fff" stroke-width="2"/></svg>Link 1</li>
<li><svg width="11" height="8" viewBox="0 0 11 8"><path d="M0 0l4 4-4 4M5 0l4 4-4 4" fill="none" stroke="#fff" stroke-width="2"/></svg>Link 1</li></ul></div>
<div class="abs fcol" style="left:322px"><h4>About Us</h4><ul>
<li><svg width="11" height="8" viewBox="0 0 11 8"><path d="M0 0l4 4-4 4M5 0l4 4-4 4" fill="none" stroke="#fff" stroke-width="2"/></svg>Link 1</li>
<li><svg width="11" height="8" viewBox="0 0 11 8"><path d="M0 0l4 4-4 4M5 0l4 4-4 4" fill="none" stroke="#fff" stroke-width="2"/></svg>Link 1</li>
<li><svg width="11" height="8" viewBox="0 0 11 8"><path d="M0 0l4 4-4 4M5 0l4 4-4 4" fill="none" stroke="#fff" stroke-width="2"/></svg>Link 1</li>
<li><svg width="11" height="8" viewBox="0 0 11 8"><path d="M0 0l4 4-4 4M5 0l4 4-4 4" fill="none" stroke="#fff" stroke-width="2"/></svg>Link 1</li>
<li><svg width="11" height="8" viewBox="0 0 11 8"><path d="M0 0l4 4-4 4M5 0l4 4-4 4" fill="none" stroke="#fff" stroke-width="2"/></svg>Link 1</li></ul></div>
<div class="abs fcol" style="left:479px"><h4>Our Services</h4><ul>
<li><svg width="11" height="8" viewBox="0 0 11 8"><path d="M0 0l4 4-4 4M5 0l4 4-4 4" fill="none" stroke="#fff" stroke-width="2"/></svg>Link 1</li>
<li><svg width="11" height="8" viewBox="0 0 11 8"><path d="M0 0l4 4-4 4M5 0l4 4-4 4" fill="none" stroke="#fff" stroke-width="2"/></svg>Link 1</li>
<li><svg width="11" height="8" viewBox="0 0 11 8"><path d="M0 0l4 4-4 4M5 0l4 4-4 4" fill="none" stroke="#fff" stroke-width="2"/></svg>Link 1</li>
<li><svg width="11" height="8" viewBox="0 0 11 8"><path d="M0 0l4 4-4 4M5 0l4 4-4 4" fill="none" stroke="#fff" stroke-width="2"/></svg>Link 1</li>
<li><svg width="11" height="8" viewBox="0 0 11 8"><path d="M0 0l4 4-4 4M5 0l4 4-4 4" fill="none" stroke="#fff" stroke-width="2"/></svg>Link 1</li></ul></div>
<div class="abs fcol" style="left:638px"><h4>Crews</h4><ul>
<li><svg width="11" height="8" viewBox="0 0 11 8"><path d="M0 0l4 4-4 4M5 0l4 4-4 4" fill="none" stroke="#fff" stroke-width="2"/></svg>Link 1</li>
<li><svg width="11" height="8" viewBox="0 0 11 8"><path d="M0 0l4 4-4 4M5 0l4 4-4 4" fill="none" stroke="#fff" stroke-width="2"/></svg>Link 1</li>
<li><svg width="11" height="8" viewBox="0 0 11 8"><path d="M0 0l4 4-4 4M5 0l4 4-4 4" fill="none" stroke="#fff" stroke-width="2"/></svg>Link 1</li>
<li><svg width="11" height="8" viewBox="0 0 11 8"><path d="M0 0l4 4-4 4M5 0l4 4-4 4" fill="none" stroke="#fff" stroke-width="2"/></svg>Link 1</li>
<li><svg width="11" height="8" viewBox="0 0 11 8"><path d="M0 0l4 4-4 4M5 0l4 4-4 4" fill="none" stroke="#fff" stroke-width="2"/></svg>Link 1</li></ul></div>
<div class="abs fcol" style="left:772px;top:1045px"><h4>Find Us on :</h4></div>
<div class="abs social">
  <span style="background:#5bb8e6"></span><span style="background:#3b63b0"></span><span style="background:#2a62c4"></span>
  <span style="background:#f08a1e"></span><span style="background:#2a62c4"></span>
</div>
<div class="abs footbar">Copyright © 2010 lensharborteutonia</div>
</body>
</html>
```